Poster Design for kebab shop products

need a new poster for our new velmo pack special, sign will be inside of shopping centre at different location to shop will need to stand out and draw customers to the store, MUST contain shops logo & picture added, poster size will be 76cm x 101cm so will need to suit that size

MUST ALSO CONTAIN THE FOLLOWING
Velmo Pack / HSP
Lamb & Chips
Chicken & Chips
Beef & Chips
+ Can $15

Target Market(s)

new customers

Industry/Entity Type

Retail

Font styles to use
Sans Serif

Colors

Designer to choose colors to be used in the design.

Requirements
Must have
• company logo
• picture of vemo pack provided
• Velmo Pack / HSP
• Lamb & Chips
• Chicken & Chips
• Beef & Chips
• + Can $15

```html
<!DOCTYPE html>
<html lang="en">
<head>
<meta charset="utf-8">
<title>Kebab Lagoon – Velmo Pack Poster</title>
<link rel="stylesheet" href="https://fonts.googleapis.com/css2?family=Arimo:wght@400;700&family=Oswald:wght@500&display=swap">
<style>
  :root {
    --page-bg: #e4e1dc;
    --sky-light: #fff6e4;
    --sky-mid: #f2ab55;
    --sky-deep: #c76d1c;
    --sun: #f49b1f;
    --brand-red: #c8161d;
    --band-red: #c4161c;
    --wood-light: #9a6038;
    --wood-mid: #6e3f22;
    --wood-dark: #2e170c;
    --label-orange: #f7a21b;
    --white: #ffffff;
    --tray: #efeeea;
    --food-meat: #6b4226;
    --food-chip: #e2b457;
    --can-red: #d3202a;
    --can-dark: #8e0e14;
  }
  * { margin: 0; padding: 0; box-sizing: border-box; }
  html, body {
    width: 1200px;
    height: 832px;
    overflow: hidden;
    background: var(--page-bg);
  }
  .poster {
    position: absolute;
    left: 306px;
    top: 26px;
    width: 588px;
    height: 780px;
    overflow: hidden;
    background: var(--wood-dark);
    font-family: "Arimo", Arial, sans-serif;
    box-shadow: 0 10px 30px rgba(0,0,0,0.25);
  }
  .poster__sky {
    position: absolute;
    inset: 0 0 auto 0;
    height: 470px;
    background:
      radial-gradient(ellipse 55% 50% at 50% 30%, var(--sky-light) 0%, #f8c982 30%, var(--sky-mid) 60%, var(--sky-deep) 100%);
  }
  .poster__floor {
    position: absolute;
    left: 0; right: 0;
    top: 420px;
    bottom: 0;
    background:
      linear-gradient(180deg, rgba(199,109,28,0) 0%, rgba(154,96,56,0.9) 14%, var(--wood-mid) 50%, var(--wood-dark) 100%);
  }
  .brand {
    position: absolute;
    left: 0; right: 0;
    top: 35px;
    height: 210px;
  }
  .brand__disc {
    position: absolute;
    left: 194px;
    top: 0;
    width: 200px;
    height: 200px;
    border-radius: 50%;
    background: var(--sun);
  }
  .brand__name {
    position: absolute;
    left: 0; right: 0;
    top: 112px;
    text-align: center;
    font-weight: 700;
    font-size: 62px;
    line-height: 1;
    color: var(--brand-red);
  }
  .product-photo {
    position: absolute;
    left: 78px;
    top: 232px;
    width: 410px;
    height: 350px;
    border-radius: 14px;
    background:
      radial-gradient(ellipse 46% 40% at 48% 52%, var(--food-chip) 0%, #b98848 38%, var(--food-meat) 62%, #a89a88 82%, var(--tray) 100%);
    box-shadow: 0 14px 24px rgba(40,20,8,0.45);
  }
  .drink-photo {
    position: absolute;
    left: 467px;
    top: 235px;
    width: 103px;
    height: 212px;
    border-radius: 16px 16px 12px 12px;
    background: linear-gradient(90deg, var(--can-dark) 0%, var(--can-red) 30%, #f26a70 52%, var(--can-red) 72%, var(--can-dark) 100%);
    box-shadow: 0 10px 18px rgba(40,20,8,0.4);
  }
  .price-badge {
    position: absolute;
    left: 396px;
    top: 463px;
    width: 143px;
    height: 143px;
    border-radius: 50%;
    background: radial-gradient(circle at 50% 40%, #e0262d 0%, var(--band-red) 70%, #9c1015 100%);
    border: 2px solid rgba(255,255,255,0.6);
    box-shadow: 0 0 0 6px var(--band-red), 0 8px 16px rgba(0,0,0,0.35);
    display: flex;
    align-items: center;
    justify-content: center;
    font-family: "Oswald", "Arial Narrow", sans-serif;
    font-weight: 500;
    font-size: 52px;
    color: var(--white);
  }
  .offer-title {
    position: absolute;
    left: 0; right: 0;
    top: 622px;
    text-align: center;
    font-size: 27px;
    font-weight: 400;
    line-height: 1;
    color: var(--label-orange);
    text-transform: uppercase;
  }
  .menu-band {
    position: absolute;
    left: 0; right: 0;
    top: 666px;
    height: 63px;
    background: var(--band-red);
    display: flex;
    align-items: center;
  }
  .menu-item {
    flex: 1;
    text-align: center;
    color: var(--white);
    font-size: 19px;
    line-height: 1.1;
    text-transform: uppercase;
    letter-spacing: 0.4px;
    padding: 2px 0;
  }
  .menu-item + .menu-item {
    border-left: 2px solid var(--white);
  }
  .menu-item__extra {
    display: block;
    font-size: 12px;
    color: var(--label-orange);
    margin-top: 4px;
  }
</style>
</head>
<body>
  <main class="poster">
    <div class="poster__sky"></div>
    <div class="poster__floor" role="img" aria-label="Timber tabletop background"></div>

    <header class="brand">
      <div class="brand__disc"></div>
      <div class="brand__name">Kebab Lagoon</div>
    </header>

    <div class="product-photo" role="img" aria-label="Velmo pack: kebab meat over chips with garlic and chilli sauce in an open takeaway box"></div>
    <div class="drink-photo" role="img" aria-label="Can of Fizzo Cola"></div>

    <div class="price-badge">$15</div>

    <h1 class="offer-title">Velmo Pack / HSP</h1>

    <section class="menu-band">
      <div class="menu-item">Lamb &amp; Chips<span class="menu-item__extra">+Can</span></div>
      <div class="menu-item">Chicken &amp; Chips<span class="menu-item__extra">+Can</span></div>
      <div class="menu-item">Beef &amp; Chips<span class="menu-item__extra">+Can</span></div>
    </section>
  </main>
</body>
</html>
```